Corporate Design für Portweinhandel
Zielgruppe
Portweinhandel, Tastings
Aufgabenstellung
Es soll entweder eine Portweinflasche mit LP drinnen, oder eine Traubenrebe mit LP drinnen, oder LP als Logo sein. Darunter soll Lindahl Portwein gerade oder im Halbkreis unter dem Logo stehen.

```html
<!DOCTYPE html>
<html lang="de">
<head>
<meta charset="utf-8">
<title>Lindahl Portwein – Corporate Design</title>
<link href="https://fonts.googleapis.com/css2?family=Montserrat:wght@600;700&family=Barlow+Condensed:wght@500;600&display=swap" rel="stylesheet">
<style>
  :root {
    --wine: #5a0f1f;
    --purple: #3b0a4a;
    --paper: #ffffff;
    --stage: #f4f2f3;
    --light: #f3eef5;
  }
  * { box-sizing: border-box; margin: 0; padding: 0; }
  html, body { width: 1200px; height: 523px; overflow: hidden; }
  body {
    background: var(--stage);
    position: relative;
    font-family: "Barlow Condensed", "Arial Narrow", sans-serif;
    color: var(--purple);
  }
  .brand-mark {
    display: flex; flex-direction: column; align-items: center; gap: 10px;
  }
  .brand-mark .dot {
    width: 14px; height: 14px; border-radius: 50%; background: var(--wine);
  }
  .brand-mark .name {
    font-family: "Montserrat", Arial, sans-serif;
    font-weight: 700;
    color: var(--wine);
    letter-spacing: 0.06em;
    text-transform: uppercase;
    white-space: nowrap;
  }

  .logo-showcase { position: absolute; left: 90px; top: 210px; width: 290px; }
  .logo-showcase .name { font-size: 24px; }

  .card {
    position: absolute; left: 440px; width: 300px; height: 194px;
    box-shadow: 2px 3px 6px rgba(0,0,0,.25);
    display: flex; flex-direction: column; align-items: center; justify-content: center;
  }
  .card-front { top: 50px; background: var(--paper); }
  .card-front .name { font-size: 17px; }
  .card-back { top: 280px; background: var(--purple); color: var(--paper); text-align: center; }
  .card-back h2 {
    font-family: "Montserrat", Arial, sans-serif; font-weight: 600;
    font-size: 14px; letter-spacing: 0.04em; margin-bottom: 14px;
  }
  .card-back p { font-size: 10.5px; letter-spacing: 0.14em; line-height: 1.6; font-weight: 600; }

  .letterhead {
    position: absolute; left: 810px; top: 20px; width: 340px; height: 483px;
    background: var(--paper); box-shadow: 2px 3px 6px rgba(0,0,0,.25);
  }
  .letterhead .brand-mark { position: absolute; top: 38px; left: 0; right: 0; gap: 6px; }
  .letterhead .dot { width: 9px; height: 9px; }
  .letterhead .name { font-size: 11px; }
  .sender-line {
    position: absolute; left: 40px; top: 88px; font-size: 4.5px; font-weight: 600;
    font-family: "Montserrat", Arial, sans-serif;
  }
  .address-block {
    position: absolute; right: 21px; top: 87px; text-align: right;
    font-size: 4.6px; line-height: 1.55; font-weight: 600; color: var(--wine);
  }
  .address-block strong {
    display: block; font-family: "Montserrat", Arial, sans-serif; font-size: 5.2px;
    color: var(--purple); margin-bottom: 2px;
  }
  .fold-mark { position: absolute; left: 0; width: 8px; height: 1px; background: var(--wine); }
  .letter-footer {
    position: absolute; left: 0; right: 0; bottom: 0; height: 47px;
    background: var(--purple); color: var(--paper);
    display: grid; grid-template-columns: 1.1fr 1.1fr 1fr;
    padding: 11px 20px 0 33px; font-size: 4.3px; line-height: 1.7; font-weight: 600;
  }
  .letter-footer strong { font-family: "Montserrat", Arial, sans-serif; font-size: 4.8px; display: block; }
</style>
</head>
<body>

  <section class="logo-showcase brand-mark">
    <span class="dot"></span>
    <span class="name">Lindahl Portwein</span>
  </section>

  <article class="card card-front">
    <div class="brand-mark">
      <span class="dot"></span>
      <span class="name">Lindahl Portwein</span>
    </div>
  </article>

  <article class="card card-back">
    <h2>LINDAHL PORTWEIN</h2>
    <p>Musterstraße 123 | 12345 Musterstadt<br>
       Tel.: 0123 45678 | Fax: 0123 456788<br>
       info@lindahlportwein.example<br>
       www.lindahlportwein.example</p>
  </article>

  <article class="letterhead">
    <div class="brand-mark">
      <span class="dot"></span>
      <span class="name">Lindahl Portwein</span>
    </div>
    <div class="sender-line">LINDAHL PORTWEIN | Musterstraße 123 | 12345 Musterstadt</div>
    <div class="address-block">
      <strong>LINDAHL PORTWEIN</strong>
      Musterstraße 123<br>
      12345 Musterstadt<br>
      Tel.: 0123 45678<br>
      Fax: 0123 456788<br>
      info@lindahlportwein.example<br>
      www.lindahlportwein.example
    </div>
    <span class="fold-mark" style="top:170px"></span>
    <span class="fold-mark" style="top:240px"></span>
    <span class="fold-mark" style="top:339px"></span>
    <footer class="letter-footer">
      <div><strong>LINDAHL PORTWEIN</strong>Musterstraße 123<br>12345 Musterstadt</div>
      <div>USt-IDNR: CHE-481.902.337 MWST</div>
      <div>Kreditbank Alpenland<br>IBAN: DE 00 1234 5678 9012 3456 7<br>Clearing: 7710<br>SWIFT/BIC: KBALCHZZ10</div>
    </footer>
  </article>

</body>
</html>
```